Book Cover Design

Design with title UNWAVERING
Subtitle: Ways to Kindle the Spark of Resolve
Author Name: Carla Jean Morrow
Put DAILY MERIDIAN BESTSELLER at top
Shimmer design, see inspirational images attached

```html
<!DOCTYPE html>
<html lang="en">
<head>
<meta charset="utf-8">
<title>Unwavering — Book Cover</title>
<link rel="stylesheet" href="https://fonts.googleapis.com/css2?family=Poppins:wght@700;800&family=Fredoka:wght@600&display=swap">
<style>
  :root {
    --page-bg: #ececec;
    --ink: #0d0d0d;
    --badge: #c8717a;
    --author: #ffffff;
    --shimmer-top: #fbe3dc;
    --shimmer-gold: #f7cdb7;
    --shimmer-peach: #f6b1a3;
    --shimmer-pink: #f1a6d8;
    --shimmer-lilac: #c6a3f0;
    --shimmer-violet: #b39bf2;
  }
  * { margin: 0; padding: 0; box-sizing: border-box; }
  html, body {
    width: 1111px;
    height: 1200px;
    overflow: hidden;
    background: var(--page-bg);
  }
  .cover {
    position: absolute;
    left: 205px;
    top: 50px;
    width: 700px;
    height: 1100px;
    overflow: hidden;
    box-shadow: 0 10px 30px rgba(0,0,0,0.12);
  }
  .cover__shimmer {
    position: absolute;
    inset: 0;
    background:
      radial-gradient(ellipse 60% 40% at 40% 25%, rgba(255,240,220,0.8), transparent 70%),
      radial-gradient(ellipse 50% 45% at 85% 55%, rgba(246,170,150,0.7), transparent 70%),
      radial-gradient(ellipse 60% 40% at 25% 85%, rgba(180,160,245,0.8), transparent 70%),
      linear-gradient(170deg, var(--shimmer-top) 0%, var(--shimmer-gold) 25%, var(--shimmer-peach) 45%, var(--shimmer-pink) 65%, var(--shimmer-lilac) 82%, var(--shimmer-violet) 100%);
  }
  .cover__badge {
    position: absolute;
    top: 140px;
    left: 0;
    right: 0;
    text-align: center;
    font-family: "Poppins", sans-serif;
    font-weight: 700;
    font-size: 31px;
    letter-spacing: 0.5px;
    color: var(--badge);
  }
  .cover__title {
    position: absolute;
    top: 490px;
    left: 0;
    right: 0;
    text-align: center;
    font-family: "Poppins", sans-serif;
    font-weight: 800;
    font-size: 76px;
    line-height: 1;
    letter-spacing: 1px;
    color: var(--ink);
  }
  .cover__subtitle {
    position: absolute;
    top: 590px;
    left: 0;
    right: 0;
    text-align: center;
    font-family: "Fredoka", sans-serif;
    font-weight: 600;
    font-size: 27px;
    color: var(--ink);
  }
  .cover__author {
    position: absolute;
    top: 990px;
    left: 0;
    right: 0;
    text-align: center;
    font-family: "Poppins", sans-serif;
    font-weight: 700;
    font-size: 25px;
    letter-spacing: 1px;
    color: var(--author);
  }
</style>
</head>
<body>
  <main class="cover">
    <div class="cover__shimmer" role="img" aria-label="Iridescent holographic foil texture shifting from peach and gold to pink and lilac"></div>
    <p class="cover__badge">DAILY MERIDIAN BESTSELLER</p>
    <h1 class="cover__title">UNWAVERING</h1>
    <p class="cover__subtitle">Ways to Kindle the Spark of Resolve</p>
    <p class="cover__author">CARLA JEAN MORROW</p>
  </main>
</body>
</html>
```